依頼詳細
アルコール除菌ジェルのラベルのデザインをお願い致します
サイズはW110mm×H154mm
ラミネート貼り
希望イメージ
シンプル 複雑
単色 カラフル
暗い 明るい
日常 高級
遊び心 厳粛
未来的 伝統的
女性的 男性的
希望する色
緑系
納品ファイル
• イラストレーター形式 (.ai)
補足説明
実際の現在のデザイン(他社)を添付致します。
添付のデザインのOEM製品になり弊社自社品となります
雰囲気を全然違うようにしてください
業務用です
添付の画像にありますKAVELは必要ございません
また発売元は弊社で製造元は別な会社で記載頂くと思います
宜しくお願い致します
容器の画像を添付致しました。
円形のPETボトルになります
販売先は自動車ディーラー様中心となります
■ 選んだ理由

ディーラー様及び通常の販売先において頂けるデザインでした
関係者で3点選びましたが、全員がこの方のデザインが上がりましたので
決定しました

■ 提案者全員のお礼・コメント

沢山の方からデザインをあげて頂き非常に迷いました。
今後もこのサイトを使って新商品のデザインや
容器のデザインをお願いしたいと思いますのでその際は
宜しいお願い致します。今回はありがとうございました

```html
<!DOCTYPE html>
<html lang="ja">
<head>
<meta charset="utf-8">
<title>アルコール除菌ジェル ラベル</title>
<link rel="stylesheet" href="https://fonts.googleapis.com/css2?family=Noto+Sans+JP:wght@400;500;700;900&family=Roboto:wght@500;700&display=swap">
<style>
  :root{
    --teal:#1fb0b5;
    --teal-dark:#0d8e98;
    --teal-pale:#c9ecec;
    --ink:#1b1b1b;
    --grey:#6b6b6b;
    --rule:#b9b9b9;
    --cell:#e9e9e9;
    --red:#d8262e;
    --paper:#ffffff;
  }
  html,body{margin:0;padding:0;overflow:hidden;background:var(--paper);}
  .canvas{position:relative;width:846px;height:1200px;background:var(--paper);font-family:"Noto Sans JP",sans-serif;color:var(--ink);overflow:hidden;}
  .file-note{position:absolute;left:16px;top:16px;font-size:9px;color:var(--grey);}
  .trim-marks{position:absolute;left:0;top:0;}
  .label{position:absolute;left:150px;top:148px;width:546px;height:900px;background:var(--paper);overflow:hidden;}
  .top-band{position:absolute;left:0;top:0;width:100%;height:22px;background:var(--teal);}
  .title{position:absolute;left:0;width:100%;text-align:center;font-weight:900;letter-spacing:2px;line-height:1;}
  .title--main{top:105px;font-size:68px;color:var(--ink);}
  .title--accent{top:190px;font-size:68px;color:var(--teal);}
  .subtitle{position:absolute;top:292px;left:0;width:100%;text-align:center;font-family:"Roboto",sans-serif;font-weight:700;font-size:24px;letter-spacing:1px;}
  .visual{position:absolute;left:0;top:335px;width:100%;height:150px;background:linear-gradient(180deg,var(--teal-pale) 0%,var(--teal) 55%,var(--teal-dark) 100%);}
  .badges{position:absolute;right:54px;top:520px;display:flex;gap:6px;align-items:center;}
  .badge-volume{border:2px solid var(--ink);font-family:"Roboto",sans-serif;font-weight:700;font-size:17px;padding:1px 6px;}
  .badge-fire{background:var(--red);color:#fff;font-weight:700;font-size:14px;padding:3px 6px;}
  .badge-note{font-size:8px;color:var(--grey);margin-left:2px;}
  .spec{position:absolute;left:22px;top:556px;width:502px;display:grid;grid-template-columns:1fr 1fr;column-gap:10px;font-size:9px;}
  .spec-row{display:grid;grid-template-columns:52px 1fr;border-bottom:1px solid var(--rule);min-height:17px;align-items:center;}
  .spec-key{background:var(--cell);height:100%;display:flex;align-items:center;padding-left:4px;font-weight:500;}
  .spec-val{padding-left:6px;}
  .notes{position:absolute;left:22px;top:650px;width:502px;font-size:8.4px;line-height:1.5;}
  .notes h3{font-size:9.5px;margin:0 0 2px;font-weight:700;}
  .notes p{margin:0 0 3px;}
  .maker{position:absolute;left:22px;top:790px;width:330px;font-size:8.4px;line-height:1.6;}
  .maker-name{display:inline-flex;align-items:center;gap:4px;font-weight:700;color:var(--red);}
  .maker-name i{display:inline-block;width:9px;height:9px;background:var(--red);}
  .marks{position:absolute;right:22px;top:790px;display:flex;gap:8px;}
  .mark{width:30px;height:30px;border:1.5px solid var(--ink);border-radius:50%;}
  .mark--square{border-radius:3px;width:46px;}
  .bottom-band{position:absolute;left:0;bottom:0;width:100%;height:12px;background:var(--teal);}
</style>
</head>
<body>
<div class="canvas">
  <div class="file-note">アルコール除菌ジェル（W110mm H154mm）</div>

  <svg class="trim-marks" width="846" height="1200" viewBox="0 0 846 1200" fill="none" stroke="#333" stroke-width="0.8">
    <path d="M150 100V135M136 148H100M696 100V135M710 148H746M150 1100V1061M136 1048H100M696 1100V1061M710 1048H746"/>
    <path d="M138 100V135M136 160H100M708 100V135M710 160H746M138 1100V1061M136 1036H100M708 1100V1061M710 1036H746"/>
    <path d="M423 100V130M423 1070V1100M100 598H128M718 598H746"/>
  </svg>

  <div class="label">
    <div class="top-band"></div>
    <div class="title title--main">アルコール</div>
    <div class="title title--accent">除菌ジェル</div>
    <div class="subtitle">ALCOHOL SANITIZER</div>

    <div class="visual" role="img" aria-label="青緑系の流れるような装飾帯"></div>

    <div class="badges">
      <span class="badge-volume">1L</span>
      <span class="badge-fire">火気厳禁</span>
      <span class="badge-note">第四類アルコール類</span>
    </div>

    <div class="spec">
      <div class="spec-row"><span class="spec-key">品　名</span><span class="spec-val">アルコール除菌ジェル</span></div>
      <div class="spec-row"><span class="spec-key">用　途</span><span class="spec-val">手指・器具の清浄</span></div>
      <div class="spec-row"><span class="spec-key">成　分</span><span class="spec-val">エタノール、水、増粘剤、保湿剤</span></div>
      <div class="spec-row"><span class="spec-key">原産国</span><span class="spec-val">日本</span></div>
      <div class="spec-row"><span class="spec-key">内容量</span><span class="spec-val">1L（1000mL）</span></div>
      <div class="spec-row"><span class="spec-key">液　性</span><span class="spec-val">中性</span></div>
      <div class="spec-row"><span class="spec-key">使用法</span><span class="spec-val">適量を手に取り、乾くまで擦り込む</span></div>
      <div class="spec-row"><span class="spec-key">保　管</span><span class="spec-val">直射日光を避け冷暗所に保管</span></div>
    </div>

    <div class="notes">
      <h3>【使用上の注意】</h3>
      <p>●火気の近くで使用しないでください。引火性があります。●目に入らないよう注意し、入った場合はすぐに水で洗い流してください。●傷口、湿疹など肌に異常がある部位には使用しないでください。●肌に合わない場合は使用を中止し、医師に相談してください。●乳幼児の手の届かない所に保管してください。</p>
      <p>●用途以外には使用しないでください。●他の容器に移し替えないでください。●使用後はキャップをしっかり閉めてください。●塗装面、樹脂面などに付着した場合はすぐに拭き取ってください。</p>
    </div>

    <div class="maker">
      <div>販売元 <span class="maker-name"><i></i>緑星商事株式会社</span></div>
      <div>東京都港区芝浦三丁目 12-4　TEL 03-0000-1234</div>
      <div>製造元 青葉ケミカル株式会社</div>
      <div>埼玉県川口市本町一丁目 5-8　TEL 048-000-5678</div>
    </div>

    <div class="marks" aria-label="リサイクル表示">
      <span class="mark"></span>
      <span class="mark"></span>
      <span class="mark mark--square"></span>
    </div>

    <div class="bottom-band"></div>
  </div>
</div>
</body>
</html>
```